Bref créative
Limb Nestler
Naturally made in the US
Professional
Rosalind Featherstone
Owner
437 Tamsin Ave - Ste 220-581
rfeatherstone@limbnestler-example.com
Limbnestler-example.com
I'm not sure what the first two boxes refer to. I want our logo to be on the cards in the same colors.

```html
<!DOCTYPE html>
<html lang="en">
<head>
<meta charset="utf-8">
<title>Limb Nestler – Business Card</title>
<link rel="stylesheet" href="https://fonts.googleapis.com/css2?family=Arimo:wght@400;700&display=swap">
<style>
  :root {
    --frame: #5e5e5e;
    --card: #ffffff;
    --maroon: #7a3437;
    --blue: #1c9ad6;
    --ink: #3d3d3d;
    --ink-soft: #555555;
  }
  * { box-sizing: border-box; margin: 0; padding: 0; }
  html, body {
    width: 1200px; height: 737px; overflow: hidden;
    background: var(--frame);
    font-family: "Arimo", Arial, sans-serif;
  }
  .card {
    position: absolute; left: 34px; top: 29px;
    width: 1137px; height: 674px;
    background: var(--card);
  }
  .brand {
    position: absolute; left: 62px; top: 70px;
    width: 360px;
  }
  .brand-dot {
    display: block;
    width: 170px; height: 170px; border-radius: 50%;
    background: var(--blue);
    margin-left: 70px;
  }
  .brand-name {
    margin-top: 18px;
    font-size: 48px; font-weight: 400; color: var(--ink);
    letter-spacing: 0.5px; line-height: 1;
  }
  .brand-tagline {
    margin-top: 4px; padding-left: 112px;
    font-size: 18px; color: var(--ink-soft); line-height: 1;
  }
  .person {
    position: absolute; left: 62px; top: 380px;
  }
  .person-name {
    font-size: 38px; font-weight: 700; color: var(--maroon); line-height: 1.1;
  }
  .person-title {
    font-size: 36px; color: var(--ink); line-height: 1.2;
  }
  .contact {
    position: absolute; left: 62px; top: 470px;
    list-style: none;
    font-size: 26px; color: var(--ink); line-height: 34px;
  }
  .contact b { font-weight: 700; }
  .footer-band {
    position: absolute; left: 0; top: 600px; width: 1137px; height: 43px;
  }
  .website {
    position: absolute; left: 62px; top: 600px; height: 43px;
    display: flex; align-items: center;
    font-size: 26px; font-weight: 700; color: #ffffff;
  }
</style>
</head>
<body>
  <main class="card">
    <div class="brand">
      <span class="brand-dot"></span>
      <p class="brand-name">limb nestler</p>
      <p class="brand-tagline">naturally made in the US</p>
    </div>

    <div class="person">
      <p class="person-name">Rosalind Featherstone</p>
      <p class="person-title">Owner</p>
    </div>

    <ul class="contact">
      <li><b>T:</b> 877-555-0148</li>
      <li><b>C:</b> 515-555-0172</li>
      <li><b>E:</b> rfeatherstone@limbnestler-example.com</li>
      <li>437 Tamsin Ave - Ste 220-581</li>
    </ul>

    <svg class="footer-band" viewBox="0 0 1137 43" aria-hidden="true">
      <polygon points="0,0 786,0 806,43 0,43" fill="var(--maroon)"/>
      <polygon points="800,0 1137,0 1137,43 822,43" fill="var(--blue)"/>
    </svg>
    <p class="website">www. Limbnestler-example.com</p>
  </main>
</body>
</html>
```